Global Careers Business Needs a Flyer Design

We need a flyer design to promote our Open Path Talks seminars.
We provide free career tools and insights to young professionals through our business Bright Harbour.

We would like to see our corporate colours utilised in the flyer
Grey R66 G73 B74
Teal R38 G128 B138
White R242 G240 B230

Attached is the flyer content, logo of our business and the image we wish to be used. Please note we would like to see two options of the image reflected in our teal corporate colour and a black and white option.

The final design should communicate a professional, eye-catching finish with a layout that captures the attention of our online users. Open to portrait or landscape layout.
Updates

Please note I will also require a JPEG file as well as the PDF for this piece of work. Added Friday, June 26, 2015

Target Market(s)

20-30's

Industry/Entity Type

Business

Font styles to use
Serif
Sans Serif
Other font styles liked:
• Calibri, Helvetica

Requirements
Must have
• Logo
• a DESIGN element -I do not wish to see the content just pasted onto the image. Please consider a design element, font styles, colours, etc
Nice to have
• Consider highlighting the quote by Helen Maddox.
Should not have
• I do not wish to see the content just pasted onto the image. Please consider a design element, font styles, colours, etc

```html
<!DOCTYPE html>
<html lang="en">
<head>
<meta charset="utf-8">
<title>Open Path Talks – Seminar Flyer</title>
<link rel="stylesheet" href="https://fonts.googleapis.com/css2?family=Arimo:wght@400;700&family=Cormorant+Garamond:wght@500&family=Oswald:wght@300&display=swap">
<style>
  :root {
    --brand-grey: #42494a;
    --brand-grey-dark: #3d4243;
    --brand-teal: #26808a;
    --brand-white: #f2f0e6;
    --sky-light: #a9dcdc;
    --sky-mid: #6fc3c8;
    --sky-deep: #2f9ca7;
    --page-bg: #e6e6e4;
  }
  * { box-sizing: border-box; margin: 0; padding: 0; }
  html, body { width: 1200px; height: 1200px; overflow: hidden; }
  body {
    background: var(--page-bg);
    display: flex;
    align-items: center;
    justify-content: center;
    font-family: "Arimo", Helvetica, Arial, sans-serif;
    color: var(--brand-white);
  }
  .flyer {
    width: 896px;
    height: 1160px;
    background: var(--brand-grey);
    display: flex;
    flex-direction: column;
  }

  /* Header */
  .intro {
    height: 336px;
    padding: 44px 42px 0 40px;
  }
  .intro__title {
    font-family: "Cormorant Garamond", Georgia, serif;
    font-weight: 500;
    font-size: 86px;
    line-height: 1;
    letter-spacing: -1px;
    white-space: nowrap;
    color: var(--brand-white);
    margin-bottom: 22px;
  }
  .intro__title-accent { color: var(--brand-teal); }
  .intro__text {
    font-size: 15.6px;
    line-height: 1.38;
    margin-bottom: 11px;
  }

  /* Photo band */
  .feature {
    position: relative;
    height: 527px;
    background: linear-gradient(160deg, var(--sky-deep) 0%, var(--sky-mid) 45%, var(--sky-light) 100%);
  }
  .feature__quote {
    position: absolute;
    left: 46px;
    top: 32px;
    width: 560px;
    padding-left: 20px;
    border-left: 5px solid rgba(242, 240, 230, 0.7);
    padding-top: 4px;
    padding-bottom: 6px;
  }
  .feature__speaker {
    font-size: 21px;
    line-height: 1.3;
    margin-bottom: 12px;
  }
  .feature__speaker strong { font-weight: 700; }
  .feature__statement {
    font-family: "Oswald", "Arial Narrow", sans-serif;
    font-weight: 300;
    font-size: 28px;
    line-height: 1.5;
  }
  .feature__mark {
    color: var(--brand-teal);
    font-family: "Oswald", "Arial Narrow", sans-serif;
    font-size: 62px;
    line-height: 0;
    vertical-align: -20px;
  }

  /* Footer content */
  .details {
    position: relative;
    height: 297px;
    padding: 42px 40px 0 40px;
  }
  .details__heading {
    color: var(--brand-teal);
    font-size: 22px;
    font-weight: 400;
    margin-bottom: 10px;
  }
  .details__list { list-style: none; margin-bottom: 18px; }
  .details__list li {
    font-size: 16px;
    line-height: 1.34;
    position: relative;
    padding-left: 10px;
  }
  .details__list li::before {
    content: "";
    position: absolute;
    left: 0;
    top: 8px;
    width: 4px;
    height: 4px;
    background: var(--brand-teal);
  }
  .details__audience {
    font-size: 16px;
    line-height: 1.34;
    width: 420px;
  }
  .brand {
    position: absolute;
    left: 496px;
    top: 100px;
    display: flex;
    align-items: center;
    gap: 24px;
  }
  .brand__dot {
    width: 52px;
    height: 52px;
    border-radius: 50%;
    border: 3px solid var(--brand-teal);
  }
  .brand__name {
    color: var(--brand-teal);
    font-weight: 700;
    font-size: 40px;
    line-height: 1.05;
    letter-spacing: 3px;
    text-transform: uppercase;
  }
  .details__rule {
    position: absolute;
    left: 0;
    right: 0;
    top: 256px;
    height: 2px;
    background: var(--brand-white);
    opacity: 0.8;
  }
  .details__band {
    position: absolute;
    left: 0;
    right: 0;
    top: 262px;
    height: 9px;
    background: var(--brand-teal);
  }
</style>
</head>
<body>
  <article class="flyer">
    <header class="intro">
      <h1 class="intro__title">OPEN PATH <span class="intro__title-accent">TALKS</span></h1>
      <p class="intro__text">Making the transition from school or university to work is no small step. In fact studies show that young people require considerable support during this early stage to ensure their employment is sustained.</p>
      <p class="intro__text">With the average person spending over 90,000 hours of their life at work, and changing jobs seven to eight times before thirty - It's critical to prepare.</p>
      <p class="intro__text">Open Path Talks is a high energy seminar that addresses key elements, often lost and forgotten in the lead up to entering the workforce.</p>
    </header>

    <section class="feature" role="img" aria-label="Teal-toned photograph of a rollercoaster track curving up into a bright cloudy sky">
      <blockquote class="feature__quote">
        <p class="feature__speaker"><strong>Helen Maddox,</strong> a passionate and outspoken former career banker turned entrepreneur delivers a message with conviction.</p>
        <p class="feature__statement"><span class="feature__mark">“</span> Young people need to view their career as the equivalent of a rollercoaster ride but believe they can control the dips and turns.<span class="feature__mark">”</span></p>
      </blockquote>
    </section>

    <footer class="details">
      <h2 class="details__heading">Open Path Talks will explore how to:</h2>
      <ul class="details__list">
        <li>Overcome setbacks at work</li>
        <li>Influence what people say about you</li>
        <li>Embrace both good and not so good feedback</li>
        <li>Start building a success story for your future</li>
      </ul>
      <p class="details__audience">This seminar is ideal for high school leavers, college graduates and developing young professionals.</p>
      <div class="brand">
        <span class="brand__dot"></span>
        <span class="brand__name">Bright<br>Harbour</span>
      </div>
      <div class="details__rule"></div>
      <div class="details__band"></div>
    </footer>
  </article>
</body>
</html>
```